Looking for a contemporary business card design with our logo

would like to consider a embossing look although I'm not married to the idea. We are a custom jeweler that needs a look that represents old world craftsmanship with a modern twist that's why we went with a more modern shield type of logo that can be stamped inside our rings.
It could be two sided or one we are more after a look the pops and is trendy and creative. (WE ARE NOT LOOKING FOR A COOKIE CUTTER LAYOUT)
We have attached the image and will be using the logo with kestrel forge wording in the format that it's in unless you see a better way of doing it.
If the logo needs a twist we are O.K. with suggestions as well.
This card should scream "Quality" from a high end studio.
Kestrel Forge
4189 Malbrook Rd. Unit C-7
Fenmoor, WA 98614
www.kestrelforge.example
mo@kestrelforge.example
Should speak quality craftsmanship

```html
<!DOCTYPE html>
<html lang="en">
<head>
<meta charset="utf-8">
<title>Kestrel Forge — Business Card</title>
<link rel="stylesheet" href="https://fonts.googleapis.com/css2?family=Open+Sans:wght@400;600&display=swap">
<style>
  :root {
    --canvas: #d9d3ca;
    --cream: #ebe6dc;
    --cream-light: #f4f1ea;
    --charcoal: #3a3a3c;
    --slate: #57575a;
    --ink: #2b2b2d;
    --taupe: #6f665b;
    --taupe-text: #8a7d6c;
    --black: #161617;
    --white: #ffffff;
    --gold-line: #8c7d66;
  }
  * { margin: 0; padding: 0; box-sizing: border-box; }
  html, body {
    width: 1200px; height: 1023px; overflow: hidden;
    background: var(--canvas);
    font-family: "Open Sans", Arial, sans-serif;
  }
  .stage { position: relative; width: 1200px; height: 1023px; }

  .card {
    position: absolute; width: 640px; height: 366px;
    border-radius: 4px; overflow: hidden;
    box-shadow: 0 10px 28px rgba(0,0,0,0.22);
  }

  /* Front */
  .card-front {
    left: 70px; top: 90px;
    background: linear-gradient(135deg, var(--cream-light), var(--cream));
  }
  .front-brand {
    position: absolute; left: 0; right: 0; top: 62px;
    display: flex; justify-content: center; align-items: center; gap: 16px;
  }
  .brand-square { width: 54px; height: 54px; background: var(--charcoal); }
  .brand-name {
    font-weight: 600; font-size: 34px; color: var(--charcoal);
    text-transform: uppercase; letter-spacing: 1px;
  }
  .front-details {
    position: absolute; left: 0; right: 0; top: 178px;
    display: flex; justify-content: center;
  }
  .person {
    text-align: right; padding-right: 20px;
    border-right: 1px solid var(--slate);
    font-size: 15px; line-height: 1.5; color: var(--slate);
  }
  .person-name { font-weight: 600; font-size: 19px; color: var(--taupe-text); }
  .contacts {
    padding-left: 20px; font-size: 15px; line-height: 1.55; color: var(--ink);
    list-style: none;
  }
  .contacts li { display: flex; align-items: center; gap: 8px; }
  .contacts svg { width: 13px; height: 13px; fill: var(--slate); }
  .front-band {
    position: absolute; left: 0; right: 0; bottom: 0; height: 62px;
    background: linear-gradient(180deg, var(--slate), var(--charcoal) 55%, var(--black));
  }
  .web-tab {
    position: absolute; right: 0; bottom: 62px; height: 40px; width: 300px;
    background: var(--taupe);
    clip-path: polygon(24px 0, 100% 0, 100% 100%, 0 100%);
    color: var(--cream); font-size: 15px;
    display: flex; align-items: center; padding-left: 50px;
  }

  /* Back */
  .card-back {
    left: 490px; top: 560px;
    background: linear-gradient(150deg, #2c2c2e, var(--black) 60%);
  }
  .back-brand {
    position: absolute; left: 0; right: 0; top: 130px;
    display: flex; justify-content: center; align-items: center; gap: 18px;
  }
  .back-brand .brand-square { background: var(--white); width: 64px; height: 64px; }
  .back-brand .brand-name { color: var(--white); font-size: 40px; }
  .back-rule {
    position: absolute; left: 40px; right: 250px; bottom: 46px;
    height: 1px; background: var(--gold-line);
  }
  .back-web {
    position: absolute; right: 40px; bottom: 36px;
    font-size: 15px; color: var(--gold-line);
  }
</style>
</head>
<body>
<main class="stage">
  <section class="card card-front">
    <div class="front-brand">
      <span class="brand-square"></span>
      <span class="brand-name">Kestrel Forge</span>
    </div>
    <div class="front-details">
      <div class="person">
        <div class="person-name">Mara Ostrow</div>
        <div>4189 Malbrook Rd.</div>
        <div>Unit C-7 Fenmoor, WA 98614</div>
      </div>
      <ul class="contacts">
        <li><svg viewBox="0 0 16 16"><path d="M3 1h3l1 4-2 1a9 9 0 0 0 5 5l1-2 4 1v3a2 2 0 0 1-2 2A13 13 0 0 1 1 3a2 2 0 0 1 2-2z"/></svg>(555)301-0142</li>
        <li><svg viewBox="0 0 16 16"><rect x="4" y="1" width="8" height="14" rx="1.5"/></svg>(555)301-0187</li>
        <li><svg viewBox="0 0 16 16"><rect x="1" y="3" width="14" height="10"/><path d="M1 3l7 6 7-6" stroke="#ebe6dc" stroke-width="1.5" fill="none"/></svg>mo@kestrelforge.example</li>
      </ul>
    </div>
    <div class="web-tab">www.kestrelforge.example</div>
    <div class="front-band"></div>
  </section>

  <section class="card card-back">
    <div class="back-brand">
      <span class="brand-square"></span>
      <span class="brand-name">Kestrel Forge</span>
    </div>
    <div class="back-rule"></div>
    <div class="back-web">www.kestrelforge.example</div>
  </section>
</main>
</body>
</html>
```